Perfect — here’s the updated version of your description with **title #1** and the integration/booking functionality references removed, while still keeping the “motivation to book” idea in the design style:
---
**Luxury Property Website Design – Dominican Republic**
We are looking to create a professional and visually appealing **website design** for a premium property that we will be promoting as a short-term rental.
The property is located in an **exclusive area of the Dominican Republic** and offers a high-end experience for guests. Our goal is to create a website that highlights the **luxury, comfort, and exclusivity** of the property, while motivating visitors to **make a reservation inquiry**.
**Key Requirements:**
* A clean, modern, and elegant design that reflects the **premium nature** of the property.
* High-quality visual presentation of the **property’s best features** (rooms, amenities, location, views, nearby attractions).
* Easy-to-navigate structure
* Mobile-friendly and optimized for all screen sizes.
* Space for testimonials or guest reviews to build trust.
**Design Style We Like:**
* Elegant and sophisticated, with a touch of tropical luxury.
* Use of high-quality photography, subtle animations, and a warm color palette that reflects the Caribbean atmosphere.
* A premium feel, similar to boutique hotel or luxury villa rental websites.
**Deliverables:**
* Homepage design.
* Property detail page design (with gallery, amenities, and booking inquiry section).
Contact page or About Us page
* Photo Gallery
The final design should capture the essence of a **luxury getaway** and make visitors feel compelled to reserve their night.

```html
<!DOCTYPE html>
<html lang="en">
<head>
<meta charset="utf-8">
<title>Solenne Villa — Luxury Villa, Dominican Republic</title>
<link href="https://fonts.googleapis.com/css2?family=Playfair+Display:wght@400&family=DM+Sans:wght@400;500&display=swap" rel="stylesheet">
<style>
  :root{
    --ink:#2a2724;
    --coral:#d8775a;
    --cream:#f4eee5;
    --sand:#ebe1d1;
    --gold:#c7a36b;
    --muted:#7c746b;
    --line:#d9cfc0;
    --serif:"Playfair Display", Georgia, serif;
    --sans:"DM Sans", Helvetica, Arial, sans-serif;
  }
  *{box-sizing:border-box;margin:0;padding:0}
  html,body{width:1200px;height:3348px;overflow:hidden}
  body{background:var(--cream);color:var(--ink);font-family:var(--sans);position:relative}
  .section{position:absolute;left:0;width:1200px}
  .heading{font-family:var(--serif);font-weight:400;line-height:1.02;letter-spacing:-0.5px}
  .photo{position:absolute}
  .book-circle{position:absolute;width:96px;height:96px;border-radius:50%;background:var(--coral);color:#fff;
    font-size:13px;font-weight:500;display:flex;align-items:center;justify-content:center;text-align:center}

  /* hero */
  .hero{top:0;height:740px}
  .brand{position:absolute;left:60px;top:42px;font-family:var(--sans);font-size:18px;font-weight:500;display:flex;align-items:center;gap:10px}
  .brand-dot{width:10px;height:10px;border-radius:50%;background:var(--ink)}
  .hero .book-circle{right:60px;top:28px}
  .hero-title{position:absolute;left:0;right:0;top:122px;text-align:center;font-size:80px}
  .hero-photo{left:60px;top:340px;width:1080px;height:390px;border-radius:0 0 40px 40px;
    background:linear-gradient(180deg,#cfd9d6 0%,#9aa79a 38%,#5f7257 62%,#7fb1b4 82%,#476450 100%)}

  /* amenities */
  .amenities{top:740px;height:660px}
  .amenities-title{position:absolute;left:60px;top:90px;font-size:50px;width:560px}
  .amenities-title span{display:block;padding-left:90px}
  .amenities-text{position:absolute;left:680px;top:100px;width:440px;font-size:14px;line-height:1.6;color:var(--muted)}
  .amenities-note{position:absolute;left:60px;top:260px;width:220px;font-size:13px;line-height:1.55;color:var(--muted)}
  .side-photo{left:0;top:390px;width:240px;height:170px;border-radius:0 90px 90px 0;
    background:linear-gradient(135deg,#8e8a6e,#5c6b4a 55%,#c9b99a)}
  .arch-photo{left:640px;top:300px;width:420px;height:320px;border-radius:210px 210px 0 0;
    background:linear-gradient(180deg,#e8ded0 0%,#c9b79c 45%,#8c7a61 75%,#5b5043 100%)}
  .amenities .book-circle{left:590px;top:460px}

  /* stats */
  .stats{top:1400px;height:170px;display:grid;grid-template-columns:repeat(4,1fr);padding:0 60px;column-gap:40px}
  .stat{border-top:1px solid var(--line);padding-top:14px}
  .stat-label{font-size:12px;color:var(--muted)}
  .stat-value{font-family:var(--serif);font-size:62px;color:var(--coral);margin-top:34px;line-height:1}
  .stat-value sup{font-family:var(--sans);font-size:14px;vertical-align:top;margin-left:4px}

  /* gallery */
  .gallery{top:1570px;height:860px}
  .gallery-title{position:absolute;left:320px;top:30px;font-size:50px;width:600px}
  .gallery-title span{display:block;padding-left:90px}
  .gallery-arrows{position:absolute;left:60px;top:80px;display:flex;gap:14px}
  .gallery-row{left:60px;top:215px;width:1080px;height:220px;display:grid;grid-template-columns:60px 1fr 24px 1fr 60px;gap:0}
  .gal{height:220px;border-radius:6px}
  .gal-a{background:linear-gradient(135deg,#a68d6c,#6f5d45)}
  .gal-b{background:linear-gradient(135deg,#e9e2d6,#bfae94 60%,#8a7660)}
  .gal-c{background:linear-gradient(135deg,#f0e8db,#c8b79f 55%,#6f7c5a)}
  .gal-d{background:linear-gradient(135deg,#7e6b52,#4f5a3c)}
  .escape-photo{left:60px;top:455px;width:1080px;height:390px;border-radius:6px;
    background:linear-gradient(180deg,#6d5a45 0%,#8a7152 35%,#3e6f72 68%,#2f5a4c 100%)}
  .escape-title{position:absolute;left:100px;top:660px;font-size:46px;color:#fff;width:420px}
  .escape-title span{display:block;padding-left:60px}

  /* testimonials */
  .stories{top:2430px;height:400px}
  .stories-title{position:absolute;left:250px;top:50px;font-size:42px;width:700px}
  .stories-title span{display:block;padding-left:60px}
  .avatar{left:250px;top:210px;width:110px;height:130px;border-radius:6px;background:linear-gradient(160deg,#e2c4a8,#b98a66)}
  .quote-mark{position:absolute;left:400px;top:208px;width:34px;height:28px}
  .review-name{position:absolute;left:400px;top:250px;font-size:14px;font-weight:500}
  .review-role{position:absolute;left:400px;top:270px;font-size:12px;color:var(--muted)}
  .review-text{position:absolute;left:400px;top:298px;width:420px;font-size:13px;line-height:1.6;color:var(--muted)}
  .stories-rule{position:absolute;left:60px;right:60px;bottom:0;border-top:1px solid var(--line)}

  /* cta */
  .cta{top:2830px;height:518px}
  .cta-title{position:absolute;left:60px;top:40px;font-size:46px;width:520px}
  .cta .book-circle{right:60px;top:60px}
  .cta-photo{left:60px;top:210px;width:1080px;height:308px;border-radius:40px 40px 0 0;
    background:linear-gradient(180deg,#dfe4dc 0%,#9fb293 40%,#5e7549 70%,#8c8f7a 100%)}
</style>
</head>
<body>

<section class="section hero">
  <div class="brand"><span class="brand-dot"></span>Solenne Villa</div>
  <a class="book-circle">Book now</a>
  <h1 class="heading hero-title">A haven beyond<br>maps and time</h1>
  <div class="photo hero-photo" role="img" aria-label="Modern two-storey villa with pool surrounded by tropical palms"></div>
</section>

<section class="section amenities">
  <h2 class="heading amenities-title">Indulgence woven <span>into every amenity</span></h2>
  <p class="amenities-text">Every detail of this tropical hideaway was shaped with your comfort in mind. Wake to the sea breeze, drift between shaded terraces and pool, and let quiet, attentive service turn every hour into something worth remembering.</p>
  <p class="amenities-note">Begin your mornings with a swim in the water-view infinity pool.</p>
  <div class="photo side-photo" role="img" aria-label="Shaded garden walkway beside the villa"></div>
  <div class="photo arch-photo" role="img" aria-label="Open living room with lounge seating facing the terrace"></div>
  <a class="book-circle">Book now</a>
</section>

<section class="section stats">
  <div class="stat"><div class="stat-label">Villa space</div><div class="stat-value">120<sup>m²</sup></div></div>
  <div class="stat"><div class="stat-label">Guests</div><div class="stat-value">14<sup>max</sup></div></div>
  <div class="stat"><div class="stat-label">Garden area</div><div class="stat-value">180<sup>m²</sup></div></div>
  <div class="stat"><div class="stat-label">Avg. temp</div><div class="stat-value">35<sup>°C</sup></div></div>
</section>

<section class="section gallery">
  <div class="gallery-arrows" aria-hidden="true">
    <svg width="20" height="20" viewBox="0 0 20 20"><path d="M12 4 6 10l6 6" fill="none" stroke="#2a2724" stroke-width="1.5"/></svg>
    <svg width="20" height="20" viewBox="0 0 20 20"><path d="M8 4l6 6-6 6" fill="none" stroke="#2a2724" stroke-width="1.5"/></svg>
  </div>
  <h2 class="heading gallery-title">A closer look at <span>your luxury gateway</span>gallery</h2>
  <div class="photo gallery-row">
    <div class="gal gal-a" role="img" aria-label="Bedroom detail"></div>
    <div class="gal gal-b" role="img" aria-label="Bright living room with sofas"></div>
    <div></div>
    <div class="gal gal-c" role="img" aria-label="Bedroom opening onto the garden"></div>
    <div class="gal gal-d" role="img" aria-label="Terrace lounge detail"></div>
  </div>
  <div class="photo escape-photo" role="img" aria-label="Covered terrace beside a lit pool in the evening"></div>
  <h2 class="heading escape-title">Luxury escape <span>in the heart of</span>the Caribbean</h2>
</section>

<section class="section stories">
  <h2 class="heading stories-title">Stories carried home <span>from the Dominican</span>sunlit shores</h2>
  <div class="photo avatar" role="img" aria-label="Guest portrait"></div>
  <svg class="quote-mark" viewBox="0 0 34 28" aria-hidden="true"><path d="M0 28V16C0 6 5 1 14 0v5c-5 1-7 4-7 9h7v14zm20 0V16C20 6 25 1 34 0v5c-5 1-7 4-7 9h7v14z" fill="#d8775a"/></svg>
  <div class="review-name">Elena Ruiz</div>
  <div class="review-role">Guest from Madrid</div>
  <p class="review-text">Our week at the villa felt like a private world. The staff anticipated everything, the sunsets from the terrace were unforgettable, and we are already planning our return.</p>
  <div class="stories-rule"></div>
</section>

<section class="section cta">
  <h2 class="heading cta-title">Ready to make an unforgettable experience for you?</h2>
  <a class="book-circle">Book now</a>
  <div class="photo cta-photo" role="img" aria-label="Garden path leading to a villa pavilion among palms"></div>
</section>

</body>
</html>
```